Pediatric Dentist Website

We need a photoshop mockup of one page of a pediatric dentist website. This site will not have an intro page. This layout will need to work for all 4 pages of the final site.

We just finished creating a logo for this practice. It should be attached.

The name of the practice is:

Pediatric Dentistry of Calloway

The doctor''s name is:

Martin Kowalczyk, DMD

There needs to have a menu with 4 pages on it.

Home

Meet the Doctor

Our Office

Contact Us

Please use sample text on the page.

A pediatric dentist is a dentist who specializes in treating kids, so feel free to use pictures of kids in the design.

Design Information:

The doctor likes the following sites:

http://www.plumtreekidsdds.example/

http://www.drmarisoldds.example/

http://drortonwhitfield.example/

http://toothgrovecorner.example/

Their office has an outdoors, woodsy, camping, rustic feel to it. He would like the website to portray that if possibly.

Please do not include stick figure people in it like the following websites:

http://www.arnoldvantedds.example/

http://littlemolarhub.example/

He does not like these sites. He called them too cartoonish.

For the address and phone, please use

742 Quarry Lane

Anytown, GA, 30987

Phone: (877) 555-0142

Fax: (877) 555-0142

If we pick your design, we will most likely need you to modify some small details on it.

We will also need the development files for this.

Fax: (877) 555-0142
Updates

Please be sure to use the logo we have provided. Also, colors should compliment the logo.

The sample design should be of the home page. You can use kids or a mom and kid(s) or a photo of "the office" as an example with the home page text.

So far the designs I''ve seen are okay. They all need a lot of work before I can present them to my client. Things to keep in mind: They will be adding pages later on to expand their website, so the menu needs to be down the left-hand side. 

Although the doctor didn''t specify this site as one of the sites he liked, I like it for an example of the format of the site: http://www.clearpebblegrins.example/. Also, this is one that the doctor did say that he liked: http://drortonwhitfield.example/

The text needs to be on a white or cream background. Having it be on other colors gets too hard to read and looks unprofessional.

Keep in mind this is going to be a full website. Most of the designs I''ve seen so far have been too small to expand into a full website.

Target Market(s)

Parents of kids and kids themselves.

```html
<!DOCTYPE html>
<html lang="en">
<head>
<meta charset="utf-8">
<title>Pediatric Dentistry of Calloway</title>
<link href="https://fonts.googleapis.com/css2?family=Arimo:ital,wght@0,400;0,700;1,400&family=Chewy&display=swap" rel="stylesheet">
<style>
  :root {
    --page-bg: #f7f7f7;
    --sky-top: #4cc6f6;
    --sky-mid: #7fd3f7;
    --grass: #4f8a2a;
    --grass-light: #8cc24a;
    --panel-cream: #fffcf2;
    --panel-edge: #e6dcc0;
    --nav-active: #1a8fd0;
    --nav-active-edge: #0d6fae;
    --text-white: #ffffff;
    --heading: #1677b8;
    --body-text: #2e3b44;
    --intro-text: #4a5a66;
    --photo-light: #f4f6f7;
    --photo-dark: #c3ced6;
    --ink: #111111;
  }
  * { margin: 0; padding: 0; box-sizing: border-box; }
  html, body { width: 1200px; height: 698px; overflow: hidden; }
  body { background: var(--page-bg); font-family: "Arimo", Arial, sans-serif; position: relative; }

  .site-frame {
    position: absolute; left: 120px; top: 24px; width: 960px; height: 636px;
    border-radius: 12px; overflow: hidden;
    box-shadow: 0 0 6px rgba(0,0,0,0.25);
  }
  .scenery {
    position: absolute; inset: 0;
    background: linear-gradient(180deg, var(--sky-top) 0%, var(--sky-mid) 58%, #b9e6f9 70%, var(--grass-light) 82%, var(--grass) 100%);
  }

  .sidebar { position: absolute; left: 20px; top: 30px; width: 216px; }
  .brand {
    height: 170px;
    display: flex; flex-direction: column; align-items: center; justify-content: center; gap: 12px;
    text-align: center;
  }
  .brand-mark { width: 56px; height: 56px; border-radius: 50%; background: var(--text-white); }
  .brand-name { color: var(--text-white); font-weight: 700; font-size: 21px; line-height: 1.2; }

  .main-nav { list-style: none; margin-top: 28px; }
  .main-nav li { margin-bottom: 8px; }
  .main-nav a {
    display: block; font-family: "Chewy", cursive; font-size: 25px; color: var(--text-white);
    text-decoration: none; height: 44px; line-height: 42px; padding: 0 16px;
    border: 1px solid transparent; border-radius: 5px;
    text-shadow: 0 0 2px rgba(0,40,90,0.6);
  }
  .main-nav a.is-current { background: var(--nav-active); border-color: var(--nav-active-edge); }

  .content-panel {
    position: absolute; left: 258px; top: 26px; width: 680px; height: 584px;
    background: var(--panel-cream); border: 1px solid var(--panel-edge); border-radius: 12px;
    padding: 20px 22px;
    color: var(--body-text);
  }
  .content-panel h1 {
    color: var(--heading); font-size: 17px; font-weight: 700; line-height: 22px; margin-bottom: 10px;
  }
  .doctor-photo {
    float: right; width: 218px; height: 285px; margin: 0 0 12px 22px;
    border: 3px solid var(--text-white); border-radius: 12px;
    box-shadow: 0 0 4px rgba(0,0,0,0.2);
    background: linear-gradient(160deg, var(--photo-light) 0%, #d9e2e8 55%, var(--photo-dark) 100%);
  }
  .copy { font-size: 12.5px; line-height: 16px; letter-spacing: 0.2px; margin-bottom: 14px; }
  .copy.intro { font-style: italic; color: var(--intro-text); text-indent: 44px; }

  .footer-note { position: absolute; top: 672px; width: 100%; text-align: center; font-size: 13px; color: var(--ink); }
</style>
</head>
<body>
  <div class="site-frame">
    <div class="scenery" role="img" aria-label="Blue sky with clouds over green grass and white daisies"></div>

    <aside class="sidebar">
      <div class="brand">
        <span class="brand-mark"></span>
        <span class="brand-name">Pediatric Dentistry of Calloway</span>
      </div>
      <ul class="main-nav">
        <li><a class="is-current" href="#">Home</a></li>
        <li><a href="#">Meet the Doctor</a></li>
        <li><a href="#">Our Office</a></li>
        <li><a href="#">Contact Us</a></li>
      </ul>
    </aside>

    <main class="content-panel">
      <h1>About Martin Kowalczyk, DMD</h1>
      <div class="doctor-photo" role="img" aria-label="Portrait photo of the dentist in a white coat"></div>
      <p class="copy intro">As a specialist in the field of Pediatric Dentistry, Dr. Kowalczyk has completed an advanced program of education. After receiving his doctorate of dental surgery in 1993 at Harrow State University, Brookfield, Dr. Kowalczyk completed his two-year Pediatric Dentistry residency program at the Medical College of Eastbrook in Linden.</p>
      <p class="copy">Dr. Kowalczyk started his career as a Pediatric Dentist in Anchorage, Alaska. The beauty and grandeur of this untouched wilderness has left a wonderful, lasting impression on Dr. Kowalczyk and his family. As a result, Dr. Kowalczyk desired to bring a sample of the Alaskan wilderness back to Augusta with many of the small details of his office.</p>
      <p class="copy">Dr. Kowalczyk takes an active role in meeting and exceeding the standards of his profession. He is an active member of the National Guild of Pediatric Dentistry, National Dental Circle, State Dental Fellowship, Eastern District Dental Society and Southern Society of Child Dentistry.</p>
      <p class="copy">Dr. Kowalczyk continues to attend numerous pediatric education seminars each year to keep him in the forefront of Pediatric Dentistry. Dr. Kowalczyk gave a presentation at the annual National Guild of Pediatric Dentistry "String of Pearls" lecture in 2003.</p>
      <p class="copy">Dr. Kowalczyk is blessed with a beautiful wife, Rhona and four wonderful children, Martin Jr., Mae Ellis, Alder, and Bram.</p>
      <p class="copy">To contact Dr. Kowalczyk, please give him a call or send him an email at office@drortonwhitfield.example.</p>
    </main>
  </div>

  <p class="footer-note">Copyright © 2008 Pediatric Dentist.</p>
</body>
</html>
```